Brand-new Pediatric Dental Practice needs a website

We are a brand-new dental practice that will specialize in treating children. We want a gorgeous and easily navigable dental practice website that would make a good first impression to potential patients and their parents. It should be modern, SEO-friendly, mobile responsive, and optimized to win new patients.

Target Market(s)

Parents

Industry/Entity Type

Healthcare/Dentistry

Coding

Coded - Design and coding required

Number of Pages Required

4 page

Requirements
Must have
• Use the Wix website building platform. 4 pages: home, meet our dentists, services, contact us
Nice to have
• has a link to our facebook, instagram

```html
<!DOCTYPE html>
<html lang="en">
<head>
<meta charset="utf-8">
<title>Maple Grove Pediatric Dentistry</title>
<link href="https://fonts.googleapis.com/css2?family=Nunito+Sans:wght@400;600;700;800&family=Arimo:ital,wght@0,400;1,400&display=swap" rel="stylesheet">
<style>
:root{
  --green:#2e8f46;
  --green-mid:#55b063;
  --green-light:#6cc07a;
  --green-deep:#237a3a;
  --ink:#333;
  --muted:#666;
  --footer:#2c2c2c;
  --white:#fff;
}
*{margin:0;padding:0;box-sizing:border-box}
html,body{width:1200px;height:4815px;overflow:hidden}
body{position:relative;background:var(--white);font-family:"Nunito Sans",sans-serif;color:var(--ink)}
.abs{position:absolute}
.body-text{font-family:"Arimo",sans-serif}

/* header */
.site-header{left:0;top:0;width:1200px;height:131px;border-top:4px solid var(--green-light);border-bottom:1px solid #e2e2e2;background:var(--white)}
.brand{left:102px;top:14px;width:170px;text-align:center}
.brand-mark{width:56px;height:56px;border-radius:50%;background:var(--green-light);margin:0 auto 4px}
.brand-name{font-size:26px;font-weight:600;color:#333;line-height:1;white-space:nowrap}
.brand-sub{font-size:8px;letter-spacing:3px;color:#333;font-weight:600;margin-top:3px;white-space:nowrap}
.btn-pill{height:48px;border-radius:24px;background:var(--green);color:#fff;font-size:13px;font-weight:700;display:flex;align-items:center;justify-content:center;gap:6px;top:26px}
.btn-login{left:757px;width:105px;background:var(--green-mid)}
.btn-book{left:873px;width:213px}
.main-nav{top:98px;left:632px;font-size:12.5px;font-weight:700}
.main-nav a{text-decoration:none;color:#222;position:absolute;white-space:nowrap}
.main-nav a.active{color:var(--green)}

/* hero */
.hero{left:0;top:131px;width:1200px;height:686px;background:linear-gradient(100deg,#d9e8f0 0%,#f3d7c4 45%,#c9a487 70%,#3b7fb6 100%)}
.hero-title{left:112px;top:288px;font-size:58px;font-weight:800;color:var(--green);letter-spacing:1px;line-height:1}
.hero-sub{left:112px;top:372px;font-size:37px;font-weight:700;color:#222;line-height:1}
.btn-read{left:112px;top:439px;width:165px;height:54px;border-radius:27px;background:var(--green);color:#fff;font-size:16px;font-weight:700;display:flex;align-items:center;justify-content:center}

/* feature cards */
.feature{top:686px;height:264px;color:#fff;text-align:center;border-bottom:6px solid rgba(0,0,0,.18)}
.feature svg{margin-top:46px}
.feature-small{font-size:18px;font-weight:600;margin-top:18px;line-height:1}
.feature-big{font-size:26px;font-weight:800;letter-spacing:.5px;margin-top:6px}
.f1{left:112px;width:312px;background:var(--green-light)}
.f2{left:443px;width:315px;background:var(--green-mid)}
.f3{left:776px;width:314px;background:var(--green)}

/* section titles */
.sec-title{left:0;width:1200px;text-align:center;font-size:36px;font-weight:700;line-height:1}
.sec-rule{width:36px;height:3px;background:var(--green);left:582px}

/* about */
.about-col{width:464px;font-size:12.6px;line-height:25.6px;color:#444;text-align:justify}
.about-col p+p{margin-top:15px}

/* services */
.services{left:0;top:1520px;width:1200px;height:682px;background:linear-gradient(120deg,#2f9148,#3aa352 50%,#2c8c45)}
.svc{width:473px;height:149px;background:rgba(255,255,255,.14)}
.svc svg{position:absolute;left:28px;top:32px}
.svc h3{position:absolute;left:121px;top:30px;color:#fff;font-size:18.5px;font-weight:600;letter-spacing:.5px}
.svc p{position:absolute;left:122px;top:68px;width:310px;color:#eef7ef;font-size:12.5px;line-height:25.6px}

/* dentists */
.dentist-photo{top:2333px;height:308px;width:310px}
.dentist-name{top:2664px;width:310px;text-align:center;font-size:20px;font-weight:700}
.dentist-role{top:2700px;width:310px;text-align:center;font-size:15px;color:var(--muted)}
.btn-details{top:2742px;width:310px;height:56px;color:#fff;font-size:16px;font-weight:700;letter-spacing:.5px;display:flex;align-items:center;justify-content:center;background:var(--green)}

/* video */
.video{left:0;top:2890px;width:1200px;height:471px;background:linear-gradient(90deg,#1d4f8a,#4f86bd 30%,#e4c3ad 50%,#2b65a3 80%,#173e74)}
.play{left:553px;top:3080px;width:94px;height:94px;border-radius:50%;background:rgba(60,60,60,.7);border:3px solid rgba(255,255,255,.5)}

/* testimonials */
.clients{left:0;top:3361px;width:1200px;height:417px;background:var(--green)}
.quote{top:3500px;width:280px;text-align:center;color:#fff}
.quote-mark{font-family:Georgia,serif;font-size:90px;font-weight:700;line-height:60px;height:50px}
.quote p{font-family:"Arimo",sans-serif;font-style:italic;font-size:13px;line-height:25.6px;margin-top:20px}
.quote-name{font-size:17px;font-weight:700;margin-top:12px}

/* contact */
.contact-head{width:460px;text-align:center;font-size:24px;font-weight:700;top:3940px}
.contact-lines{width:460px;text-align:center;font-family:"Arimo",sans-serif;font-size:13.5px;line-height:25.5px;top:3990px;color:#222}
.map{left:183px;top:4112px;width:832px;height:346px;background:linear-gradient(135deg,#e8eddc,#f1efe6 50%,#dfe6d6)}

/* footer */
.site-footer{left:0;top:4519px;width:1200px;height:296px;background:var(--footer)}
.footer-bar{left:0;top:4805px;width:1200px;height:10px;background:var(--green)}
.foot-brand{left:211px;top:4548px;width:280px;text-align:center;color:#fff}
.foot-brand .brand-mark{width:90px;height:90px}
.foot-brand .brand-name{color:#fff;font-size:40px;font-weight:600}
.foot-brand .brand-sub{color:#fff;font-size:13px;letter-spacing:5px}
.socials{left:258px;top:4720px;display:flex;gap:28px}
.socials span{width:18px;height:18px;border-radius:50%;background:#fff;display:block}
.copy{left:150px;top:4752px;width:400px;text-align:center;color:#fff;font-size:14px;font-family:"Arimo",sans-serif}
.field{left:617px;width:400px;height:39px;background:#fff;font-family:"Arimo",sans-serif;font-size:12px;color:#555;padding:12px 14px}
.btn-submit{left:617px;top:4725px;width:400px;height:40px;background:var(--green-mid);color:#fff;font-size:15px;font-weight:700;display:flex;align-items:center;justify-content:center}
</style>
</head>
<body>

<header class="abs site-header">
  <div class="abs brand">
    <div class="brand-mark"></div>
    <div class="brand-name">maple grove</div>
    <div class="brand-sub">PEDIATRIC DENTISTRY</div>
  </div>
  <div class="abs btn-pill btn-login">
    <svg width="14" height="14" viewBox="0 0 14 14"><circle cx="7" cy="7" r="6" fill="none" stroke="#fff" stroke-width="1.4"/><circle cx="7" cy="5.5" r="2" fill="#fff"/></svg>LOGIN</div>
  <div class="abs btn-pill btn-book">BOOK AN APPOINTMENT</div>
  <nav class="abs main-nav">
    <a class="active" style="left:0">HOME</a>
    <a style="left:82px">MEET OUR DENTISTS</a>
    <a style="left:261px">SERVICES</a>
    <a style="left:368px">CONTACT US</a>
  </nav>
</header>

<section class="abs hero" role="img" aria-label="Photo of a smiling child at a dental check-up with a dental mirror"></section>
<div class="abs hero-title">MAPLE GROVE</div>
<div class="abs hero-sub">PEDIATRIC DENTISTRY</div>
<div class="abs btn-read">READ MORE</div>

<div class="abs feature f1">
  <svg width="80" height="84" viewBox="0 0 80 84" fill="none" stroke="#fff" stroke-width="3"><path d="M20 10c8-6 14 0 20 2 6-2 12-8 20-2 10 8 6 24 2 32-3 7-2 30-10 30-6 0-5-22-12-22s-6 22-12 22c-8 0-7-23-10-30-4-8-8-24 2-32z"/></svg>
  <div class="feature-small">GENERAL</div><div class="feature-big">DENTISTRY</div>
</div>
<div class="abs feature f2">
  <svg width="90" height="84" viewBox="0 0 90 84" fill="none" stroke="#fff" stroke-width="3"><path d="M28 40c6-4 11 0 17 1 6-1 11-5 17-1 8 6 4 18 1 24-2 5-2 16-7 16-4 0-4-12-11-12s-7 12-11 12c-5 0-5-11-7-16-3-6-7-18 1-24z"/><path d="M40 6h22v8H48v10h-8z"/><path d="M45 24v12"/></svg>
  <div class="feature-small">COSMETIC</div><div class="feature-big">DENTISTRY</div>
</div>
<div class="abs feature f3">
  <svg width="80" height="84" viewBox="0 0 80 84" fill="none" stroke="#fff" stroke-width="3"><rect x="6" y="22" width="68" height="52" rx="6"/><path d="M28 22v-10h24v10"/><path d="M34 38h12v8h8v12h-8v8H34v-8h-8V46h8z"/></svg>
  <div class="feature-small">EMERGENCY</div><div class="feature-big">DENTAL CARE</div>
</div>

<h2 class="abs sec-title" style="top:1018px">ABOUT US</h2>
<div class="abs sec-rule" style="top:1066px"></div>
<div class="abs about-col body-text" style="left:112px;top:1112px">
  <p>Sed ut perspiciatis unde omnis iste natus error sit voluptatem accusantium doloremque laudantium, totam rem aperiam, eaque ipsa quae ab illo invent ore veritatis et quasi architecto beatae vitae dicta sunt explicabo. Nemo enim ipsam voluptatem quia voluptas sit aspernatur aut odit aut fugit, sed quia cons equuntur magni dolores eos qui ratione voluptatem sequi nesciunt. Neque porro quisquam est, qui dolorem ipsum quia dolor sit amet, consectet ur, adipisci velit, sed quia non numquam eius modi tempora incidunt ut labore et dolore magnam aliquam quaerat voluptatem.</p>
  <p>Nemo enim ipsam voluptatem quia voluptas sit aspernatur aut odit aut fugit, sed quia cons equuntur magni dolores eos qui ratione voluptatem sequi nesciunt. Neque porro quisquam est, qui dolorem ipsum quia dolor sit amet, consectet ur, adipisci velit, sed quia non numquam eius modi tempora incidunt ut labore et dolore magnam aliquam quaerat voluptatem.</p>
</div>
<div class="abs about-col body-text" style="left:626px;top:1112px">
  <p>Sed ut perspiciatis unde omnis iste natus error sit voluptatem accusantium doloremque laudantium, totam rem aperiam, eaque ipsa quae ab illo invent ore veritatis et quasi architecto beatae vitae dicta sunt explicabo. Nemo enim ipsam voluptatem quia voluptas sit aspernatur aut odit aut fugit, sed quia cons equuntur magni dolores eos qui ratione voluptatem sequi nesciunt. Neque porro quisquam est, qui dolorem ipsum quia dolor sit amet, consectet ur, adipisci velit, sed quia non numquam eius modi tempora incidunt ut labore et dolore magnam aliquam quaerat voluptatem.</p>
  <p>Emo enim ipsam voluptatem quia voluptas sit aspernatur aut odit aut fugit, sed quia cons equuntur magni dolores eos qui ratione voluptatem sequi nesciunt. Neque porro quisquam est, qui dolorem ipsum quia dolor sit amet, incidunt ut labore et dolore magnam aliquam quaerat voluptatem.</p>
</div>

<section class="abs services"></section>
<h2 class="abs sec-title" style="top:1570px;color:#fff">OUR SERVICES</h2>
<div class="abs sec-rule" style="top:1618px;background:#fff"></div>

<div class="abs svc" style="left:112px;top:1660px">
  <svg width="66" height="40" viewBox="0 0 66 40" fill="none" stroke="#fff" stroke-width="2"><path d="M4 12c4-4 8 0 10 0s6-4 10 0v16c-4 4-8 0-10 0s-6 4-10 0zM24 12c4-4 8 0 10 0s6-4 10 0v16c-4 4-8 0-10 0s-6 4-10 0zM44 12c4-4 8 0 10 0s6-4 10 0v16c-4 4-8 0-10 0s-6 4-10 0z"/><path d="M2 20h62"/></svg>
  <h3>ROUTINE EXAMS</h3><p>Sed ut perspiciatis unde omnis iste natus error sit volupta tem accusantium doloremque.</p></div>
<div class="abs svc" style="left:617px;top:1660px">
  <svg width="70" height="50" viewBox="0 0 70 50" fill="none" stroke="#fff" stroke-width="2"><rect x="4" y="4" width="36" height="24" rx="4"/><path d="M10 4v12M16 4v12M22 4v12M28 4v12M34 4v12"/><path d="M4 32h56c4 0 6 4 4 8H8c-4 0-6-4-4-8z"/></svg>
  <h3>DENTAL HYGIENE</h3><p>Sed ut perspiciatis unde omnis iste natus error sit volupta tem accusantium doloremque.</p></div>
<div class="abs svc" style="left:112px;top:1826px">
  <svg width="56" height="80" viewBox="0 0 56 80" fill="none" stroke="#fff" stroke-width="2.5"><path d="M20 2h14M27 2v12"/><path d="M10 22c6-4 12 0 18 1 6-1 12-5 18-1 8 6 4 22 0 30-2 6-2 24-8 24-5 0-4-18-10-18s-5 18-10 18c-6 0-6-18-8-24-4-8-8-24 0-30z"/></svg>
  <h3>DENTAL FILLINGS</h3><p>Sed ut perspiciatis unde omnis iste natus error sit volupta tem accusantium doloremque.</p></div>
<div class="abs svc" style="left:617px;top:1826px">
  <svg width="60" height="72" viewBox="0 0 60 72" fill="none" stroke="#fff" stroke-width="2.5"><path d="M12 6c6-4 12 0 18 1 6-1 12-5 18-1 8 6 4 18 0 24H12C8 24 4 12 12 6z"/><path d="M18 32h24M18 40h24M20 48h20M24 56h12M28 56v12"/></svg>
  <h3>DENTURES &amp; VENEERS</h3><p>Sed ut perspiciatis unde omnis iste natus error sit volupta tem accusantium doloremque.</p></div>
<div class="abs svc" style="left:112px;top:1992px">
  <svg width="70" height="62" viewBox="0 0 70 62" fill="none" stroke="#fff" stroke-width="2.5"><path d="M4 22h40l14 14v14H4z"/><circle cx="16" cy="52" r="5"/><circle cx="48" cy="52" r="5"/><path d="M18 30v12M12 36h12"/><path d="M36 4v8M28 8l4 4M44 8l-4 4"/></svg>
  <h3>EMERGENCY DENTISTRY</h3><p>Sed ut perspiciatis unde omnis iste natus error sit volupta tem accusantium doloremque.</p></div>
<div class="abs svc" style="left:617px;top:1992px">
  <svg width="80" height="62" viewBox="0 0 80 62" fill="none" stroke="#fff" stroke-width="2"><path d="M4 26c12-6 60-6 72 0-2 10-4 20-12 22H16C8 46 6 36 4 26z"/><path d="M16 26v22M28 24v24M40 24v24M52 24v24M64 26v22"/><path d="M60 4v10M55 9h10M44 10v6M41 13h6"/></svg>
  <h3>TEETH WHITENING</h3><p>Sed ut perspiciatis unde omnis iste natus error sit volupta tem accusantium doloremque.</p></div>

<h2 class="abs sec-title" style="top:2254px">MEET OUR DENTISTS</h2>
<div class="abs sec-rule" style="top:2302px"></div>

<div class="abs dentist-photo" style="left:112px;background:linear-gradient(160deg,#c9d7de,#eef2f4)" role="img" aria-label="Portrait of a dentist in a white coat"></div>
<div class="abs dentist-photo" style="left:445px;background:linear-gradient(160deg,#d6dadb,#f2f2f0)" role="img" aria-label="Portrait of an orthodontist in a clinic"></div>
<div class="abs dentist-photo" style="left:779px;background:linear-gradient(160deg,#cfd9df,#f4f6f7)" role="img" aria-label="Portrait of a hygienist in a white coat"></div>

<div class="abs dentist-name" style="left:112px">ALEX RIVERA</div>
<div class="abs dentist-name" style="left:445px">ALEX RIVERA</div>
<div class="abs dentist-name" style="left:779px">ALEX RIVERA</div>
<div class="abs dentist-role" style="left:112px">Tooth Sepcialist</div>
<div class="abs dentist-role" style="left:445px">Orthodontist</div>
<div class="abs dentist-role" style="left:779px">Hygienist</div>
<div class="abs btn-details" style="left:112px">VIEW DETAILS</div>
<div class="abs btn-details" style="left:445px;background:var(--green-mid)">VIEW DETAILS</div>
<div class="abs btn-details" style="left:779px">VIEW DETAILS</div>

<section class="abs video" role="img" aria-label="Video still of a laughing child during a dental exam"></section>
<div class="abs play"><svg width="88" height="88" viewBox="0 0 88 88"><path d="M36 28l24 16-24 16z" fill="#fff"/></svg></div>

<section class="abs clients"></section>
<h2 class="abs sec-title" style="top:3409px;color:#fff">HAPPY CLIENTS</h2>
<div class="abs sec-rule" style="top:3456px;background:#fff"></div>
<div class="abs quote" style="left:131px"><div class="quote-mark">&ldquo;</div><p>Sed ut perspiciatis unde omnis iste natus error sit voluptatem accusantium dolorem que laudantium, totam rem aperiam, eaque ipsa quae ab illo inventore veritatis et quasi vitae dicta sunt explicabo</p><div class="quote-name">Alex Rivera</div></div>
<div class="abs quote" style="left:458px"><div class="quote-mark">&ldquo;</div><p>Sed ut perspiciatis unde omnis iste natus error sit voluptatem accusantium dolorem que laudantium, totam rem aperiam, eaque ipsa quae ab illo inventore veritatis et quasi vitae dicta sunt explicabo</p><div class="quote-name">Alex Rivera</div></div>
<div class="abs quote" style="left:785px"><div class="quote-mark">&ldquo;</div><p>Sed ut perspiciatis unde omnis iste natus error sit voluptatem accusantium dolorem que laudantium, totam rem aperiam, eaque ipsa quae ab illo inventore veritatis et quasi vitae dicta sunt explicabo</p><div class="quote-name">Alex Rivera</div></div>

<h2 class="abs sec-title" style="top:3826px">CONTACT US</h2>
<div class="abs sec-rule" style="top:3874px"></div>
<div class="abs contact-head" style="left:138px">OUR ADDRESS</div>
<div class="abs contact-lines" style="left:138px">27 Orchard Lane Suite 4<br>Fairview CA 95999<br>hello@maplegrove-example.com \\ Tel: +1 555 010 0199</div>
<div class="abs" style="left:600px;top:3940px;width:1px;height:125px;background:#ccc"></div>
<div class="abs contact-head" style="left:585px">OPENING HOURS</div>
<div class="abs contact-lines" style="left:585px">Monday – Friday &nbsp;9AM – 7PM<br>Saturday &nbsp;&nbsp;&nbsp;9AM – 2PM</div>
<div class="abs map" role="img" aria-label="Street map showing the practice location with several pins"></div>

<footer class="abs site-footer"></footer>
<div class="abs foot-brand">
  <div class="brand-mark"></div>
  <div class="brand-name">maple grove</div>
  <div class="brand-sub">PEDIATRIC DENTISTRY</div>
</div>
<div class="abs socials" aria-label="Social links"><span></span><span></span><span></span><span></span></div>
<div class="abs copy">© Copyrights 2022.All Rights Reserved.</div>
<div class="abs field" style="top:4585px">Name :</div>
<div class="abs field" style="top:4632px">Email :</div>
<div class="abs field" style="top:4678px">Message :</div>
<div class="abs btn-submit">SUBMIT</div>
<div class="abs footer-bar"></div>

</body>
</html>
```